Business Cards

I'd like help creating business cards with the full logo "Veltrona Capital Partners" on the back of the card (navy background with white writing), and abbreviated logo "VCP" on the front. Would like to list name, title, phone number, email, and website listed on front of card. Would like to keep very simple. Front font Arial or similar.

```html
<!DOCTYPE html>
<html lang="en">
<head>
<meta charset="UTF-8">
<title>Veltrona Capital Partners – Business Cards</title>
<link href="https://fonts.googleapis.com/css2?family=Montserrat:wght@400;500;700;800&display=swap" rel="stylesheet">
<style>
  :root {
    --navy: #1f3669;
    --navy-deep: #1b3a70;
    --silver: #d3d5da;
    --paper: #ffffff;
    --ink: #1c1c1c;
    --backdrop: #3b3b3b;
    --logo-light: #e3e7f0;
  }
  * { margin: 0; padding: 0; box-sizing: border-box; }
  html, body {
    width: 1200px; height: 1200px; overflow: hidden;
    background: var(--backdrop);
    font-family: "Montserrat", Arial, sans-serif;
  }
  .sheet {
    position: relative; width: 1200px; height: 1200px;
    display: flex; flex-direction: column; align-items: center; justify-content: center; gap: 50px;
  }
  .card {
    position: relative; width: 900px; height: 514px; border-radius: 34px; overflow: hidden;
    box-shadow: 0 14px 30px rgba(0,0,0,.35);
  }
  /* Back */
  .card-back { background: var(--navy); display: flex; align-items: center; justify-content: center; }
  .back-brand { display: flex; align-items: center; gap: 18px; color: var(--logo-light); }
  .back-brand .mark-square { width: 24px; height: 24px; background: var(--logo-light); }
  .back-brand .brand-name { font-weight: 500; font-size: 38px; letter-spacing: 3px; text-transform: uppercase; }

  /* Front */
  .card-front { background: var(--paper); }
  .front-wave { position: absolute; left: 0; top: 0; width: 900px; height: 514px; }
  .front-brand {
    position: absolute; left: 80px; top: 120px; display: flex; align-items: center; gap: 16px;
    color: var(--navy-deep);
  }
  .front-brand .mark-square { width: 26px; height: 26px; background: var(--navy-deep); }
  .front-brand .brand-initials { font-weight: 500; font-size: 60px; letter-spacing: 8px; line-height: 1; }
  .person { position: absolute; left: 150px; top: 270px; }
  .person .name { font-weight: 800; font-size: 34px; color: var(--navy-deep); }
  .person .title { font-weight: 400; font-size: 21px; color: var(--ink); margin-top: 2px; padding-left: 36px; }
  .contact {
    position: absolute; left: 555px; top: 80px; color: var(--ink); font-size: 18px; line-height: 1.3;
  }
  .contact .address { margin-bottom: 20px; }
  .contact ul { list-style: none; padding-left: 22px; }
  .contact li { display: flex; align-items: center; gap: 14px; margin-bottom: 8px; }
  .contact svg { width: 20px; height: 20px; fill: var(--navy-deep); flex: none; }
</style>
</head>
<body>
<main class="sheet">
  <section class="card card-back" aria-label="Card back">
    <div class="back-brand">
      <span class="mark-square"></span>
      <span class="brand-name">Veltrona Capital Partners</span>
    </div>
  </section>

  <section class="card card-front" aria-label="Card front">
    <svg class="front-wave" viewBox="0 0 900 514" preserveAspectRatio="none" aria-hidden="true">
      <path d="M0 440 Q 500 430 900 280 L900 514 L0 514 Z" fill="var(--silver)"/>
      <path d="M0 456 Q 510 448 900 302 L900 514 L0 514 Z" fill="var(--navy-deep)"/>
    </svg>

    <div class="front-brand">
      <span class="mark-square"></span>
      <span class="brand-initials">VCP</span>
    </div>

    <div class="person">
      <div class="name">Daniel Okafor</div>
      <div class="title">Managing Director</div>
    </div>

    <div class="contact">
      <div class="address">418 Harbor Point Ave, #310<br>Brookfield, OH 44120</div>
      <ul>
        <li>
          <svg viewBox="0 0 24 24"><path d="M6.6 10.8a15.1 15.1 0 0 0 6.6 6.6l2.2-2.2c.3-.3.7-.4 1-.2 1.1.4 2.3.6 3.6.6.6 0 1 .4 1 1V20c0 .6-.4 1-1 1A17 17 0 0 1 3 4c0-.6.4-1 1-1h3.5c.6 0 1 .4 1 1 0 1.3.2 2.5.6 3.6.1.3 0 .7-.2 1z"/></svg>
          877-555-0148
        </li>
        <li>
          <svg viewBox="0 0 24 24"><path d="M2 5h20v14H2z M2 5l10 8 10-8" /></svg>
          info@veltronacp.com
        </li>
        <li>
          <svg viewBox="0 0 24 24"><circle cx="12" cy="12" r="10"/></svg>
          www.veltronacp.com
        </li>
      </ul>
    </div>
  </section>
</main>
</body>
</html>
```